Fresh Website for PLIM and Qulo alliance

Page designs for 11 pages using existing Jigsaw template for the homepage and existing company logo.

Mock-up of front page attached, feel free to turn it into something elegant, professional and clean.

Target Market(s)

1. Small to medium business owners who use DRUK or other accounting software who want to use Qulo.
2 Businesses who want to hire a decent Bookkeeper instead of trying to do it on the kitchen table at night.

Industry/Entity Type

It Company

Font styles to use
Sans Serif

Colors
86cae6
32a6d6
34a7d8
cee9f5

Requirements
Must have
• Use the Qulo blue colour for the website theme - PMS: Blue #00A0C6
Use the Jigsaw template design and theme - pieces of the puzzle all fitting together with Qulo and PLIM
Same font used in the plim blue png uploaded and plimtraining logo
Nice to have
• A style that mirrors and links easily with the Qulo website:
check out www.qulo.com.au
Should not have
• Cheesy pictures of money and $$,
Cluttered feel
Chunky anime like images for buttons icons
Not to scream Jigsaw and make everything look like a kids website - just subtle nods to the theme

```html
<!DOCTYPE html>
<html lang="en">
<head>
<meta charset="utf-8">
<title>Contact Us – Plim Training</title>
<link rel="stylesheet" href="https://fonts.googleapis.com/css2?family=Questrial&display=swap">
<style>
:root{
  --brand:#00a0c6;
  --brand-dark:#1a6fa8;
  --brand-light:#86cae6;
  --footer-bar:#1386a6;
  --page-bg:#efefef;
  --text:#333;
  --muted:#999;
  --field-border:#dcdcdc;
}
*{box-sizing:border-box;margin:0;padding:0}
html,body{width:942px;height:1200px;overflow:hidden}
body{position:relative;background:var(--page-bg);font-family:"Questrial",sans-serif;color:var(--text)}
.abs{position:absolute}
.top-rule{left:0;top:0;width:942px;height:5px;background:var(--brand)}
.site-header{left:0;top:5px;width:942px;height:110px;background:linear-gradient(#fff,#f1f1f1);border-bottom:1px solid #d8d8d8}
.brand{left:63px;top:28px;display:flex;align-items:center;gap:8px}
.brand-mark{width:16px;height:16px;background:var(--brand)}
.brand-name{font-size:30px;color:var(--brand);letter-spacing:.5px;line-height:1}
.main-nav a{position:absolute;top:55px;font-size:15px;color:var(--brand);text-decoration:none;letter-spacing:.8px;white-space:nowrap}
.page-band{left:0;top:115px;width:942px;height:70px;background:var(--brand)}
.page-title{left:84px;top:133px;font-size:28px;color:#fff;letter-spacing:2px;font-weight:400}
.band-pointer{left:120px;top:184px}
.intro-heading{left:84px;top:251px;font-size:20px;color:var(--brand);letter-spacing:1.2px;font-weight:400}
.intro-text{left:84px;top:285px;width:420px;font-size:13px;line-height:13px;letter-spacing:1px;color:#333}
.field-label{font-size:12px;color:#333;letter-spacing:.6px}
.field-label span{color:var(--muted)}
.field{background:#fff;border:1px solid var(--field-border);border-bottom-width:2px;font-size:12px;color:var(--muted);padding:0 8px;display:flex;align-items:center;letter-spacing:.8px}
.field.textarea{align-items:flex-start;padding-top:9px}
.select-btn{right:-1px;top:-1px;width:32px;height:31px;background:var(--brand);display:flex;align-items:center;justify-content:center}
.btn{height:28px;color:#fff;font-size:11px;letter-spacing:.8px;display:flex;align-items:center;justify-content:center}
.btn.send{background:var(--brand)}
.btn.reset{background:var(--brand-dark)}
.contact-line{left:543px;width:310px;font-size:13.5px;line-height:17px;color:var(--muted);letter-spacing:.8px}
.contact-line b{font-weight:400;color:var(--brand)}
.map{left:536px;top:505px;width:307px;height:197px;background:linear-gradient(135deg,#e3ead6 0%,#e8e6e1 45%,#e6e4df 100%)}
.site-footer{left:0;top:989px;width:942px;height:177px;background:var(--brand)}
.footer-heading{font-size:16px;color:#fff;letter-spacing:1px;font-weight:400}
.footer-rule{height:1px;background:rgba(255,255,255,.45)}
.quick a{position:absolute;font-size:11.5px;color:#fff;text-decoration:none;letter-spacing:.9px;line-height:17px}
.footer-brand{left:398px;top:1042px;width:151px;height:71px;display:flex;align-items:center;justify-content:center;gap:8px}
.footer-brand .brand-mark{background:var(--brand-light)}
.footer-brand .brand-name{color:var(--brand-light)}
.newsletter{left:639px;top:1055px;width:155px;height:27px;background:#fff;border-radius:2px;font-size:10.5px;color:#555;letter-spacing:.6px;display:flex;align-items:center;padding-left:8px}
.newsletter .go{position:absolute;right:3px;top:3px;width:22px;height:21px;background:var(--brand);color:#fff;font-size:10px;display:flex;align-items:center;justify-content:center;border-radius:2px}
.social{top:1102px;width:20px;height:20px;border-radius:50%;background:#fff}
.footer-bar{left:0;top:1166px;width:942px;height:34px;background:var(--footer-bar)}
.legal{top:1176px;font-size:10px;color:#fff;letter-spacing:.8px}
</style>
</head>
<body>
<div class="abs top-rule"></div>
<header class="abs site-header"></header>
<div class="abs brand"><span class="brand-mark"></span><span class="brand-name">plim training</span></div>
<nav class="main-nav">
  <a style="left:346px">Home</a>
  <a style="left:422px">About</a>
  <a style="left:500px">Initial Consultation</a>
  <a style="left:679px">Clients</a>
  <a style="left:762px">Contact</a>
  <a style="left:862px">Blog</a>
</nav>

<div class="abs page-band"></div>
<h1 class="abs page-title">CONTACT US</h1>
<svg class="abs band-pointer" width="32" height="26" viewBox="0 0 32 26"><path d="M0 0H32L16 26Z" fill="var(--brand)"/></svg>

<h2 class="abs intro-heading">PLIM is based in Sydney, Australia.</h2>
<p class="abs intro-text">Contact us anytime Monday to Friday during business hours (8.30 am – 5.30 pm) at the following:</p>

<form class="contact-form">
  <label class="abs field-label" style="left:86px;top:357px">Firstname <span>(Required)</span></label>
  <div class="abs field" style="left:85px;top:379px;width:166px;height:29px">First name here...</div>
  <label class="abs field-label" style="left:273px;top:357px">Subject <span>(Required)</span></label>
  <div class="abs field" style="left:273px;top:379px;width:167px;height:30px">Please Choose...
    <span class="abs select-btn"><svg width="9" height="6" viewBox="0 0 9 6"><path d="M0 0H9L4.5 6Z" fill="#fff"/></svg></span>
  </div>
  <label class="abs field-label" style="left:86px;top:419px">Email Address</label>
  <div class="abs field" style="left:85px;top:440px;width:166px;height:30px">Email Address here...</div>
  <label class="abs field-label" style="left:276px;top:419px">Contact Number</label>
  <div class="abs field" style="left:275px;top:440px;width:166px;height:30px">xxxx-xxxx-xxx</div>
  <label class="abs field-label" style="left:86px;top:485px">Message</label>
  <div class="abs field textarea" style="left:85px;top:507px;width:356px;height:187px">Your Message here...</div>
  <div class="abs btn send" style="left:85px;top:719px;width:128px">SEND MESSAGE</div>
  <div class="abs btn reset" style="left:223px;top:719px;width:128px">RESET FORM</div>
</form>

<p class="abs contact-line" style="top:363px"><b>Phone:</b> 02 5550 1847</p>
<p class="abs contact-line" style="top:396px"><b>Email:</b> books@plim.com.au</p>
<p class="abs contact-line" style="top:429px"><b>Address:</b> Corner of Marlow Street &amp; Fenwick Lane, Level 1, 12b Marlow Street, Harbour Vale NSW 2071</p>
<div class="abs map" role="img" aria-label="Street map showing the office location"></div>

<footer class="abs site-footer"></footer>
<h3 class="abs footer-heading" style="left:138px;top:1014px">Quicklinks</h3>
<div class="abs footer-rule" style="left:138px;top:1039px;width:176px"></div>
<nav class="quick">
  <a style="left:142px;top:1050px">❯ Home</a>
  <a style="left:142px;top:1076px">❯ Services</a>
  <a style="left:142px;top:1103px">❯ Initial<br>&nbsp;&nbsp;&nbsp;Consultation</a>
  <a style="left:248px;top:1050px">❯ Clients</a>
  <a style="left:248px;top:1076px">❯ Contact</a>
  <a style="left:248px;top:1102px">❯ Blog</a>
</nav>
<div class="abs footer-brand"><span class="brand-mark"></span><span class="brand-name">plim training</span></div>
<h3 class="abs footer-heading" style="left:640px;top:1013px">Keep in touch</h3>
<div class="abs footer-rule" style="left:633px;top:1039px;width:172px"></div>
<div class="abs newsletter">Email Address<span class="go">go</span></div>
<span class="abs social" style="left:641px"></span>
<span class="abs social" style="left:669px"></span>
<span class="abs social" style="left:696px"></span>
<span class="abs social" style="left:724px"></span>

<div class="abs footer-bar"></div>
<p class="abs legal" style="left:62px">Site Map &nbsp;|&nbsp; News &nbsp;|&nbsp; Privacy &nbsp;|&nbsp; Terms Of Use &nbsp;|&nbsp; About</p>
<p class="abs legal" style="right:98px">Copyright © 2014 Plim Training</p>
</body>
</html>
```